Coaching business needs flyer for business market

I need a flyer that I can send to HR-managers and business owners to inform them of my coaching services for organisations. We have three services: organisational- and teamcoaching, individual coaching and training programs.
I want the flyer to express calmness, solid and trustworthy coaching. As a person I am open and think out of the box.

In my logo I use a couple of colours (blue, green, orange and grey) that represent the diversity of humans. My company's name is Bramblecrest Engagement & Coaching and tag line is "Awaken your quiet river".

I do not want the design to be too busy but also not too boring. I tried making something myself. Feel free to build on that design. Or feel free to start from scratch.

```html
<!DOCTYPE html>
<html lang="nl">
<head>
<meta charset="utf-8">
<title>Bramblecrest Engagement &amp; Coaching – Flyer</title>
<link href="https://fonts.googleapis.com/css2?family=Ubuntu:wght@400;500;700&display=swap" rel="stylesheet">
<style>
:root{
  --coral:#ee7a62;
  --blue:#2f6b94;
  --green:#8ed3b6;
  --green-dark:#5fb895;
  --orange:#f4a12c;
  --grey:#7b7b7b;
  --text:#333;
  --paper:#fff;
}
*{box-sizing:border-box;margin:0;padding:0}
html,body{width:928px;height:1200px;overflow:hidden;background:var(--paper)}
body{font-family:"Ubuntu",Arial,sans-serif;color:var(--text)}
.flyer{position:relative;width:928px;height:1200px;overflow:hidden;background:var(--paper)}
.abs{position:absolute}
.header-decor{left:0;top:0;width:560px;height:190px;
  background:linear-gradient(100deg,rgba(142,211,182,.18),rgba(47,107,148,.12) 45%,rgba(244,161,44,.10) 75%,rgba(255,255,255,0));}
.portrait{left:116px;top:4px;width:168px;height:168px;border-radius:50%;
  background:linear-gradient(160deg,#8a6a58,#4a3a36 50%,#2f6b94);}
.brand{left:574px;top:30px;width:300px;text-align:center;color:var(--grey)}
.brand-dot{display:block;margin:0 auto 8px;width:62px;height:62px;border-radius:50%;border:3px solid var(--grey)}
.brand-name{font-size:50px;font-weight:400;letter-spacing:.5px;line-height:1;text-align:left}
.brand-sub{font-size:23px;font-weight:400;margin-top:6px;text-align:right;padding-right:8px}
.band{top:200px;height:28px;display:flex;align-items:center;font-size:19px;color:#fff}
.band-name{left:0;width:403px;background:var(--coral);justify-content:center}
.band-name b{font-weight:700;margin-right:6px}
.band-tag{left:403px;width:525px;background:var(--blue);justify-content:center;letter-spacing:4px;font-size:18px;color:#e6f0f6}
.intro-icon{left:24px;top:286px}
.intro{left:118px;top:240px;list-style:none;font-size:19.5px;line-height:31.5px}
.intro li{padding-left:28px;position:relative}
.intro li::before{content:"✓";position:absolute;left:0;color:var(--coral);font-weight:700}
.section-title{height:29px;display:flex;align-items:center;padding-left:10px;color:#fff;font-size:20px;font-weight:500}
.t-org{left:24px;top:413px;width:276px;background:var(--coral)}
.t-ind{left:558px;top:413px;width:347px;background:var(--green);color:#1f3b33;justify-content:center;border-radius:3px}
.t-train{left:29px;top:708px;width:370px;background:var(--blue)}
.t-best{left:447px;top:761px;width:343px;background:var(--orange)}
.photo{border-radius:6px}
.p-org{left:33px;top:458px;width:158px;height:200px;border:3px solid #f4b3a5;background:linear-gradient(160deg,#c9b5a0,#8d7c6e 60%,#5e6e7a)}
.p-ind{left:500px;top:467px;width:165px;height:207px;border:3px solid var(--green);background:linear-gradient(170deg,#ddd8cf,#a8a39a 60%,#6c6a66)}
.p-train{left:33px;top:754px;width:367px;height:234px;border:3px solid var(--blue);background:radial-gradient(ellipse at 55% 55%,#6b6f82,#2b2d38 60%,#16171d)}
.p-best{left:445px;top:975px;width:433px;height:206px;border:3px solid var(--orange);border-radius:10px;background:linear-gradient(180deg,#e4e2dd,#b9b2aa 55%,#6e6660)}
.list{list-style:none;font-size:18.5px;line-height:24px}
.list li{position:relative;padding-left:30px;margin-bottom:12px}
.list li::before{content:"";position:absolute;left:0;top:4px;width:16px;height:16px;border-radius:50%;border:2px solid currentColor;background:radial-gradient(circle,currentColor 0 3px,transparent 3.5px)}
.list span{color:var(--text)}
.l-org{left:205px;top:462px;width:262px;color:var(--coral)}
.l-ind{left:680px;top:467px;width:245px;color:var(--green-dark)}
.l-ind li{margin-bottom:10px}
.l-train{left:42px;top:1012px;color:var(--blue)}
.l-train li{margin-bottom:12px}
.l-best{left:456px;top:808px;width:460px;color:var(--orange)}
.l-best li{margin-bottom:13px}
.stripe{left:0;top:1192px;width:928px;height:8px;display:flex}
.stripe i{flex:1}
</style>
</head>
<body>
<div class="flyer">
  <div class="abs header-decor" role="img" aria-label="Zachte decoratieve golflijnen in de merkkleuren"></div>
  <div class="abs portrait" role="img" aria-label="Portretfoto van de trainer en coach"></div>

  <div class="abs brand">
    <span class="brand-dot"></span>
    <div class="brand-name">bramblecrest</div>
    <div class="brand-sub">engagement &amp; coaching</div>
  </div>

  <div class="abs band band-name"><b>MARISKA DEVANAND</b> - Trainer en Coach</div>
  <div class="abs band band-tag">Awaken your quiet river</div>

  <svg class="abs intro-icon" width="70" height="64" viewBox="0 0 70 64" aria-hidden="true">
    <g stroke="#ee7a62" stroke-width="3" fill="none" stroke-linecap="round">
      <line x1="2" y1="8" x2="22" y2="8"/><line x1="2" y1="18" x2="16" y2="18"/><line x1="2" y1="28" x2="14" y2="28"/><line x1="2" y1="38" x2="16" y2="38"/>
    </g>
    <circle cx="40" cy="26" r="20" fill="none" stroke="#2f6b94" stroke-width="4"/>
    <path d="M31 26 l7 7 l12 -13" fill="none" stroke="#ee7a62" stroke-width="3.5" stroke-linecap="round"/>
    <line x1="26" y1="41" x2="14" y2="58" stroke="#2f6b94" stroke-width="6" stroke-linecap="round"/>
  </svg>
  <ul class="abs intro">
    <li>Ze heeft ruime ervaring met veranderingstrajecten binnen organisaties.</li>
    <li>Mensen omschrijven haar als ‘betrokken, warm, stevig en kordaat’.</li>
    <li>Zij helpt weerstand te overwinnen en draagt bij aan groei in zelfvertrouwen.</li>
    <li>Ze gelooft de veranderkracht van de mensen waar ze mee werkt.</li>
    <li>Ze is er om steun en richting te bieden en laat hen zelf aan het roer.</li>
  </ul>

  <svg class="abs" style="left:0;top:0" width="928" height="1200" viewBox="0 0 928 1200" aria-hidden="true">
    <g fill="none" stroke-width="3">
      <polyline points="300,427 474,427 474,683 24,683 24,440" stroke="#ee7a62"/>
      <polyline points="558,427 487,427 487,734 928,734" stroke="#8ed3b6"/>
      <polyline points="398,721 424,721 424,1192" stroke="#2f6b94"/>
      <polyline points="790,775 928,775" stroke="#f4a12c"/>
    </g>
  </svg>

  <div class="abs section-title t-org">Organisatie Team Coaching</div>
  <div class="abs photo p-org" role="img" aria-label="Foto van een team tijdens een coachingsessie"></div>
  <ul class="abs list l-org">
    <li><span>Fusie of verandering</span></li>
    <li><span>Visie &amp; strategie ontwikkelen of wijzigen</span></li>
    <li><span>Cultuur-veranderen of ontwikkelen</span></li>
    <li><span>Samenwerking bevorderen of verbeteren</span></li>
  </ul>

  <div class="abs section-title t-ind">Individuele Coaching</div>
  <div class="abs photo p-ind" role="img" aria-label="Foto van een individuele coachingsessie"></div>
  <ul class="abs list l-ind">
    <li><span>Medewerkers talent</span></li>
    <li><span>Collega’s authentieke leiderschap</span></li>
    <li><span>Mensen vooruit loopbaan</span></li>
    <li><span>Medewerkers burn-out of re-integratie</span></li>
    <li><span>Outplacement trajecten</span></li>
  </ul>

  <div class="abs section-title t-train">Trainingen &amp; Maatwerk Workshops</div>
  <div class="abs photo p-train" role="img" aria-label="Foto van een groep deelnemers in een kring tijdens een workshop"></div>
  <ul class="abs list l-train">
    <li><span>Leiderschap</span></li>
    <li><span>Communicatie</span></li>
    <li><span>“Systemische Blik’ voor professionals</span></li>
    <li><span>Conflicthantering</span></li>
  </ul>

  <div class="abs section-title t-best">Best Practices</div>
  <ul class="abs list l-best">
    <li><span>Neuro Linguïstisch Programmeren (NLP)</span></li>
    <li><span>Transactionele Analyse</span></li>
    <li><span>Organisatieopstellingen, Familieopstellingen, Psycho Traumaopstellingen</span></li>
    <li><span>Ademwerk en Lichaamswerk</span></li>
  </ul>
  <div class="abs photo p-best" role="img" aria-label="Foto van een groepssessie in een lichte vergaderruimte"></div>

  <div class="abs stripe" aria-hidden="true">
    <i style="background:var(--blue)"></i><i style="background:var(--green)"></i><i style="background:var(--coral)"></i><i style="background:var(--orange)"></i><i style="background:var(--grey)"></i><i style="background:var(--blue)"></i><i style="background:var(--green)"></i>
  </div>
</div>
</body>
</html>
```